Brookhaven Business Card

I would like to re-design my company business card. I have my main company logo (Brookhaven) which must remain unchanged and I also have a number of product brands which I would like to also show on the card in some way. The corporate company colors are Blue and Orange, see pantone colors on file. However, it is not necessary to use these colors thoroughout. I am ok with grey tones etc...

Target Market(s)

Trade Business

Industry/Entity Type

Furniture

Contact Information for Business Card

Needs to incorporate Brookhaven as the main Logo. The Torvel and Kandrel product brands within the company. These can be on the back of the card.

Font styles to use
Sans Serif

Colors
0355a3
f37122

Requirements
Must have
• Marco Velditch
• COO (Global)
• Brookhaven Pacific Holdings Inc. (4371)
• Level 3, 47 Harlow Street, Melbourne VIC 3000 Australia
• Tel: +61 3 9481 2736 Mobile: +61 427 586 204
• e-mail: marco@brookhaven-au.example
• web: www.brookhaven-au.example
Nice to have
• Should be a corporate
Should not have
• No images of furniture

```html
<!DOCTYPE html>
<html lang="en">
<head>
<meta charset="utf-8">
<title>Kandrel Business Card</title>
<link href="https://fonts.googleapis.com/css2?family=Exo+2:wght@700;800&family=Roboto:wght@300;400;500;700&display=swap" rel="stylesheet">
<style>
  :root {
    --backdrop: #5a5a5c;
    --card-dark: #404043;
    --card-light: #ffffff;
    --brand-blue: #0355a3;
    --brand-orange: #f37122;
    --ink: #3a3a3d;
    --ink-soft: #555558;
    --rule: #bdbdbd;
  }
  * { margin: 0; padding: 0; box-sizing: border-box; }
  html, body { width: 1200px; height: 900px; overflow: hidden; }
  body {
    background: var(--backdrop);
    font-family: "Roboto", Arial, sans-serif;
    position: relative;
  }
  .card {
    position: absolute;
    left: 250px;
    width: 700px;
    height: 400px;
    overflow: hidden;
    box-shadow: 0 6px 18px rgba(0,0,0,0.35);
  }
  .card-front { top: 40px; background: var(--card-dark); }
  .card-back { top: 470px; background: var(--card-light); }

  /* front */
  .front-circle {
    position: absolute;
    left: 40px; top: 110px;
    width: 180px; height: 180px;
    border-radius: 50%;
    background: var(--card-light);
  }
  .front-wordmark {
    position: absolute;
    left: 250px; top: 138px;
    color: var(--card-light);
  }
  .wordmark-name {
    font-family: "Roboto", Arial, sans-serif;
    font-weight: 700;
    font-size: 76px;
    letter-spacing: 2px;
    line-height: 1;
  }
  .wordmark-tagline {
    font-weight: 300;
    font-size: 13px;
    letter-spacing: 9px;
    margin-top: 10px;
  }

  /* back */
  .back-band { position: absolute; inset: 0; }
  .back-circle {
    position: absolute;
    left: 105px; top: 40px;
    width: 130px; height: 130px;
    border-radius: 50%;
    background: var(--card-dark);
    border: 5px solid var(--card-light);
  }
  .back-wordmark {
    position: absolute;
    left: 250px; top: 62px;
    color: var(--ink);
  }
  .back-wordmark .wordmark-name { font-size: 58px; }
  .back-wordmark .wordmark-tagline { font-size: 10px; letter-spacing: 7px; margin-top: 8px; }

  .holder {
    position: absolute;
    left: 200px; top: 252px;
    width: 230px;
  }
  .holder-name {
    font-family: "Exo 2", Arial, sans-serif;
    font-weight: 800;
    font-size: 24px;
    color: var(--ink);
    letter-spacing: 0.5px;
    white-space: nowrap;
  }
  .holder-name .surname { color: var(--brand-blue); }
  .holder-role {
    font-weight: 400;
    font-size: 16px;
    color: var(--ink);
    margin-top: 4px;
    letter-spacing: 0.5px;
  }
  .divider {
    position: absolute;
    left: 440px; top: 190px;
    width: 1px; height: 160px;
    background: var(--rule);
  }
  .contact {
    position: absolute;
    left: 458px; top: 196px;
    font-size: 12.5px;
    line-height: 19px;
    color: var(--ink-soft);
    white-space: nowrap;
  }
  .contact-label { color: var(--brand-blue); font-weight: 500; }
  .address { margin-top: 26px; }
</style>
</head>
<body>

<section class="card card-front">
  <div class="front-circle"></div>
  <div class="front-wordmark">
    <div class="wordmark-name">KANDREL</div>
    <div class="wordmark-tagline">LIFETIME WARRANTY</div>
  </div>
</section>

<section class="card card-back">
  <svg class="back-band" width="700" height="400" viewBox="0 0 700 400" aria-hidden="true">
    <path d="M0 60 L75 0 C110 120 150 260 170 400 L0 400 Z" fill="var(--brand-blue)"/>
    <path d="M88 0 L116 0 C150 120 186 260 200 400 L182 400 C164 260 124 120 88 0 Z" fill="var(--brand-orange)"/>
  </svg>
  <div class="back-circle"></div>
  <div class="back-wordmark">
    <div class="wordmark-name">KANDREL</div>
    <div class="wordmark-tagline">LIFETIME FRAME WARRANTY</div>
  </div>

  <div class="holder">
    <div class="holder-name">MARCO <span class="surname">VELDITCH</span></div>
    <div class="holder-role">COO (GLOBAL)</div>
  </div>

  <div class="divider"></div>

  <div class="contact">
    <div><span class="contact-label">Tel:</span> +61 3 9481 2736</div>
    <div><span class="contact-label">Mobile:</span> +61 427 586 204</div>
    <div><span class="contact-label">E-mail:</span> marco@brookhaven-au.example</div>
    <div><span class="contact-label">Web:</span> www.brookhaven-au.example</div>
    <div class="address">
      <div>Level 3, 47 Harlow Street, Melbourne</div>
      <div>VIC 3000 Australia</div>
    </div>
  </div>
</section>

</body>
</html>
```